Crestmoor Valor Cleaning Solutions

Need a logo and business card design. I want to use a translucent business card. I want to abbreviate the name C.V.C.S. Commercial Cleaning, because my is Tam. I’d also like to incorporate a knight or something like that. I want the idea to tie in with the word Crestmoor. New ideas are welcome, i don’t want to limit anyone’s creativity.

Target Market(s)

Commercial Cleaning for businesses.

Contact Information for Business Card

Crestmoor
Valor
Cleaning
Solutions

```html
<!DOCTYPE html>
<html lang="en">
<head>
<meta charset="utf-8">
<title>Crestmoor Valor Cleaning Solutions – Business Card</title>
<link href="https://fonts.googleapis.com/css2?family=Roboto:wght@400&display=swap" rel="stylesheet">
<style>
  :root {
    --page-bg: #e9e5df;
    --card-dark: #2f2d2c;
    --card-mid: #4a4745;
    --card-edge: rgba(255,255,255,0.35);
    --ink-light: #e2d8cc;
    --ink-soft: #cfc5b9;
    --mark-dark: #1f1e1d;
  }
  * { margin: 0; padding: 0; box-sizing: border-box; }
  html, body {
    width: 1200px; height: 1047px; overflow: hidden;
    background: var(--page-bg);
  }
  .business-card {
    position: absolute; left: 100px; top: 251px;
    width: 1000px; height: 545px;
    border-radius: 22px; overflow: hidden;
    background: linear-gradient(100deg, var(--card-dark) 0%, var(--card-mid) 55%, var(--card-dark) 100%);
    border: 1px solid var(--card-edge);
    font-family: "Roboto", sans-serif;
  }
  .brand-block {
    position: absolute; left: 52px; top: 70px;
    display: flex; align-items: center; gap: 24px;
  }
  .brand-dot {
    width: 80px; height: 80px; border-radius: 50%;
    background: var(--ink-light);
    flex: none;
  }
  .brand-name {
    width: 330px;
    font-size: 30px; line-height: 38px; font-weight: 400;
    color: var(--ink-light);
  }
  .contact-block {
    position: absolute; left: 51px; top: 275px;
    font-weight: 400; color: var(--ink-soft);
  }
  .person-name { font-size: 28px; letter-spacing: 1.5px; color: var(--ink-light); }
  .person-role { font-size: 21px; margin-top: 8px; }
  .address { font-size: 21px; line-height: 34px; margin-top: 24px; }
  .contact-line { display: flex; align-items: center; gap: 14px; font-size: 21px; }
  .contact-line.phone { margin-top: 20px; }
  .contact-line.email { margin-top: 9px; }
  .contact-line svg { width: 16px; height: 16px; fill: none; stroke: var(--ink-soft); stroke-width: 1.6; }
  .side-shape {
    position: absolute; left: 665px; top: 60px;
    width: 420px; height: 420px; border-radius: 50%;
    background: var(--mark-dark);
  }
</style>
</head>
<body>
  <div class="business-card">
    <div class="brand-block">
      <div class="brand-dot"></div>
      <div class="brand-name">Crestmoor Valor Cleaning Solutions</div>
    </div>

    <div class="contact-block">
      <div class="person-name">TAMSIN HALE</div>
      <div class="person-role">CEO/Founder</div>
      <div class="address">415 W Ridgeline Rd<br>Oakfield, NC 28790</div>
      <div class="contact-line phone">
        <svg viewBox="0 0 16 16" aria-hidden="true"><path d="M4 1.5l2.5 3-1.5 1.5c.8 2 2.5 3.7 4.5 4.5L11 9l3 2.5-1.5 2.5C7 14 2 9 2 3z"/></svg>
        <span>980-555-0147</span>
      </div>
      <div class="contact-line email">
        <svg viewBox="0 0 16 16" aria-hidden="true"><rect x="1.5" y="3.5" width="13" height="9"/><path d="M1.5 3.5l6.5 5 6.5-5"/></svg>
        <span>CVCSCommercialCleaning@mailhub.com</span>
      </div>
    </div>

    <div class="side-shape"></div>
  </div>
</body>
</html>
```